Bright and beautiful business card for a coach

I'm a personal and business coach based in Perth, Australia. I need a business card that whilst subtle and elegant, will stand out and appeal on a table full of cards.

My business name is Fern Coaching and the business card must represent the warmth and brightness implied in the name, without being gimmicky. It must have a warmth and appeal and be easy to read.

I prefer clean, minimalist designs.

It must align with the feel of my website and socials: https://www.ferncoachingplex.com.au/
https://www.instagram.com/ferncoachingplexau/
https://www.facebook.com/ferncoachingplexau
Updates

Deadline appearing 2 days away and still haven't completed brief - seems mighty short

Hi Designers Thank you so much for taking the time to submit designs. I wonder if I could have explained myself a little better. Most of the designs that have been submitted look rather formal and many have quite corporate looking embellishments on them (to my eye). I would like softer, warmer, more organic. I’m open to people playing about and being more abstract, using softer embellishments (e.g the line drawing flowers and grasses I’ve used in my socials) incorporating other colours from my palette or like the social icons in my email signature (in PDF), perhaps playing with size/oversize, playing with the bleed. Please don’t be constrained by what I’ve already done, it merely needs to compliment. I’m sorry if I’m not using the right words or have led you astray. I’m no designer, but I’ve done my website, socials, email signature etc all myself (my logo was a design contest) and I was really hoping for my business card to be something more creative than I could have made with a template. Reminder: No black cards/sides please. Thank you 😊

Target Market(s)

Individuals, most likely but not all female. Creative thinkers. Likely professionals.

Industry/Entity Type

Business & Personal Coach

Contact Information for Business Card

(Fern Coaching Logo) Name: Marla Pendry; Title: Business & Personal Coach; Phone number: +61 (0)498 315807; Email: marla@ferncoachingplex.com.au; Website: https://ferncoachingplex.com.au; Social icons for Facebook, Instagram & LinkedIn: @ferncoachingplexAU. Optional strapline: "A thinking partner to help you cut through the noise"

Font styles to use
Sans Serif

Colors
00AB8E
00BBA5
67D7C9
C6EFE9
E9F9F6
59FF00
82FF00
B8FF75
E3FFCB
F4FFEA
FFC000
F8CF3A
FAE287
FDF2CF
FEFAEE

Requirements
Must have
• Must align with feel of my website and socials. Must have a pop of #FFC000 (possibly whole of one side, or at least a block). Bright or white background. Easy to read.
Nice to have
• Possibly incorporate the sunshine/grass picture I have used in website and socials - will upload.
Should not have
• Must not be black or dark. Not impersonal or corporate looking.

```html
<!DOCTYPE html>
<html lang="en">
<head>
<meta charset="utf-8">
<title>Fern Coaching – Business Card</title>
<link href="https://fonts.googleapis.com/css2?family=Open+Sans:ital,wght@0,400;0,600;0,700;1,700&display=swap" rel="stylesheet">
<style>
  :root {
    --gold: #d9961f;
    --gold-band: #d69a22;
    --gold-text: #c98a1a;
    --ink: #2a2a2a;
    --grey: #6b6b6b;
    --white: #ffffff;
    --stage: #eceae6;
    --grass-dark: #3f5a1e;
    --grass: #6f8f2c;
    --sun: #fbe3c2;
  }
  * { box-sizing: border-box; margin: 0; padding: 0; }
  html, body { width: 1200px; height: 900px; overflow: hidden; }
  body {
    background: var(--stage);
    font-family: "Open Sans", sans-serif;
    display: flex;
    flex-direction: column;
    align-items: center;
    justify-content: center;
    gap: 34px;
  }
  .card {
    width: 700px;
    height: 400px;
    position: relative;
    overflow: hidden;
    box-shadow: 0 6px 20px rgba(0,0,0,.15);
  }

  /* Front */
  .card-front { background: var(--white); }
  .front-brand {
    position: absolute;
    left: 60px;
    top: 110px;
    width: 280px;
    display: flex;
    align-items: center;
    gap: 12px;
  }
  .brand-dot {
    width: 18px; height: 18px; border-radius: 50%;
    background: var(--gold);
    flex: none;
  }
  .brand-name {
    font-weight: 600;
    font-size: 34px;
    color: var(--gold-text);
    letter-spacing: .5px;
  }
  .divider {
    position: absolute;
    left: 360px;
    top: 80px;
    width: 1.5px;
    height: 200px;
    background: var(--gold);
  }
  .contact {
    position: absolute;
    left: 385px;
    top: 86px;
  }
  .contact-name {
    font-weight: 700;
    font-size: 24px;
    color: var(--gold-text);
    text-transform: uppercase;
    letter-spacing: .3px;
  }
  .contact-title {
    font-size: 16px;
    color: var(--grey);
    margin-bottom: 14px;
  }
  .contact-list { list-style: none; }
  .contact-list li {
    display: flex;
    align-items: center;
    gap: 8px;
    font-size: 15px;
    color: var(--grey);
    line-height: 26px;
  }
  .contact-list svg { width: 13px; height: 13px; flex: none; fill: var(--gold); }
  .social-square { width: 11px; height: 11px; background: var(--gold); flex: none; margin: 0 1px; }
  .strap-band {
    position: absolute;
    left: 0; right: 0;
    top: 305px;
    height: 52px;
    background: var(--gold-band);
    display: flex;
    align-items: center;
    padding-left: 70px;
  }
  .strapline {
    font-weight: 700;
    font-style: italic;
    font-size: 19px;
    color: var(--ink);
  }

  /* Back */
  .card-back {
    display: flex;
    align-items: center;
    justify-content: center;
  }
  .back-photo {
    position: absolute; inset: 0;
    background:
      radial-gradient(circle at 72% 18%, var(--sun) 0%, rgba(251,227,194,.75) 12%, rgba(200,170,110,.35) 28%, rgba(0,0,0,0) 45%),
      linear-gradient(180deg, var(--grass) 0%, #5c7a25 45%, var(--grass-dark) 100%);
  }
  .back-brand {
    position: relative;
    display: flex;
    align-items: center;
    gap: 14px;
  }
  .back-brand .brand-dot { background: var(--white); width: 22px; height: 22px; }
  .back-brand .brand-name { color: var(--white); font-size: 52px; }
</style>
</head>
<body>

  <section class="card card-front" aria-label="Business card front">
    <div class="front-brand">
      <span class="brand-dot"></span>
      <span class="brand-name">Fern Coaching</span>
    </div>
    <div class="divider"></div>
    <div class="contact">
      <p class="contact-name">Marla Pendry</p>
      <p class="contact-title">Business &amp; Personal Coach</p>
      <ul class="contact-list">
        <li>
          <svg viewBox="0 0 24 24" aria-hidden="true"><path d="M6.6 10.8a15.1 15.1 0 0 0 6.6 6.6l2.2-2.2a1 1 0 0 1 1-.25 11.4 11.4 0 0 0 3.6.57 1 1 0 0 1 1 1V20a1 1 0 0 1-1 1A17 17 0 0 1 3 4a1 1 0 0 1 1-1h3.5a1 1 0 0 1 1 1c0 1.25.2 2.45.57 3.57a1 1 0 0 1-.25 1z"/></svg>
          +61 (0)498 315807
        </li>
        <li>
          <svg viewBox="0 0 24 24" aria-hidden="true"><path d="M2 5h20v14H2z M2 5l10 8 10-8" fill="var(--gold)"/><path d="M2 5l10 8 10-8" fill="none" stroke="#fff" stroke-width="2"/></svg>
          marla@ferncoachingplex.com.au
        </li>
        <li>
          <svg viewBox="0 0 24 24" aria-hidden="true"><circle cx="12" cy="12" r="10"/><path d="M2 12h20M12 2c3 3 3 17 0 20M12 2c-3 3-3 17 0 20" fill="none" stroke="#fff" stroke-width="1.5"/></svg>
          ferncoachingplex.com.au
        </li>
        <li>
          <span class="social-square" aria-hidden="true"></span>
          @ferncoachingplexAU
        </li>
      </ul>
    </div>
    <div class="strap-band">
      <p class="strapline">A thinking partner to help you cut through the noise</p>
    </div>
  </section>

  <section class="card card-back" aria-label="Business card back">
    <div class="back-photo" role="img" aria-label="Close-up photograph of sunlit grass with bright sun glow"></div>
    <div class="back-brand">
      <span class="brand-dot"></span>
      <span class="brand-name">Fern Coaching</span>
    </div>
  </section>

</body>
</html>
```